Business Card design for construction company

I would like a business card design for a construction company - Harlow Constructions. I have attached the ai logo file for use. I would like the card to be very smart and clean and incorporate only white and the two colours in the logo. I would like the card to have two sides. One side can just have the logo, the other with the relevant information.

Target Market(s)

Building and Construction Clients

Industry/Entity Type

Business

Contact Information for Business Card

Name: Tom Pardoe
Company: Harlow Constructions Pty Limited
Address: 14 Mallee Crescent Carrow Vale 2093
Phone: 0427 531 068
Email: tomp@harlowbuild-example.com.au

Font styles to use
Serif
Sans Serif

Requirements
Must have
• Details noted above
• Logo as provided
• Colours as in logo
• Square edges
• A font that compliments the logo
Should not have
• Any colour other than white and those in logo
• Rounded edges

```html
<!DOCTYPE html>
<html lang="en">
<head>
<meta charset="utf-8">
<title>Harlow Constructions – Business Card</title>
<link rel="stylesheet" href="https://fonts.googleapis.com/css2?family=Roboto:wght@300;400;700&display=swap">
<style>
  :root {
    --brand-blue: #00aeef;
    --brand-charcoal: #58595b;
    --text-dark: #231f20;
    --text-muted: #6d6e71;
    --paper: #ffffff;
    --backdrop: #8c8c8c;
    --backdrop-edge: #5e5e5e;
  }
  * { box-sizing: border-box; margin: 0; padding: 0; }
  html, body { width: 1200px; height: 1200px; overflow: hidden; }
  body {
    background: radial-gradient(circle at 50% 45%, var(--backdrop) 0%, var(--backdrop-edge) 100%);
    font-family: "Roboto", Arial, sans-serif;
    position: relative;
  }
  .card {
    position: absolute;
    left: 190px;
    width: 820px;
    height: 490px;
    overflow: hidden;
    box-shadow: 0 10px 24px rgba(0,0,0,0.35);
  }
  .card--details { top: 80px; background: var(--paper); }
  .card--brand { top: 630px; background: var(--brand-charcoal); }

  .card__accent-stripe {
    position: absolute;
    left: 0; right: 0;
    bottom: 64px;
    height: 10px;
    background: var(--brand-blue);
  }
  .card__footer-band {
    position: absolute;
    left: 0; right: 0; bottom: 0;
    height: 58px;
    background: var(--brand-charcoal);
  }

  .wordmark {
    position: absolute;
    font-family: "Roboto", Arial, sans-serif;
    white-space: nowrap;
    text-transform: uppercase;
  }
  .card--details .wordmark {
    left: 44px; top: 76px;
    font-size: 22px;
    font-weight: 400;
    letter-spacing: 0.2em;
    color: var(--brand-charcoal);
  }
  .card--brand .wordmark {
    left: 50%; top: 50%;
    transform: translate(-50%, -50%);
    font-size: 40px;
    font-weight: 300;
    letter-spacing: 0.15em;
    color: var(--paper);
  }

  .person { position: absolute; left: 160px; top: 272px; }
  .person__name {
    font-weight: 700;
    font-size: 35px;
    letter-spacing: 0.04em;
    color: var(--text-dark);
    line-height: 1.1;
  }
  .person__role {
    font-weight: 300;
    font-size: 20px;
    color: var(--text-muted);
    margin-top: 4px;
  }

  .contact {
    position: absolute;
    left: 418px; top: 176px;
    font-size: 22px;
    color: var(--text-dark);
    line-height: 31px;
    list-style: none;
  }
  .contact__address { margin-bottom: 10px; }
  .contact__row { display: flex; align-items: center; }
  .contact__icon {
    width: 19px; height: 19px;
    margin-right: 10px;
    flex: none;
  }
  .contact__row--email, .contact__row--web { font-size: 21px; }
</style>
</head>
<body>

<section class="card card--details" aria-label="Business card, details side">
  <div class="card__accent-stripe"></div>
  <div class="card__footer-band"></div>

  <div class="wordmark">Harlow Constructions</div>

  <div class="person">
    <p class="person__name">Tom Pardoe</p>
    <p class="person__role">Managing Director</p>
  </div>

  <ul class="contact">
    <li class="contact__address">14 Mallee Crescent<br>Carrow Vale 2093</li>
    <li class="contact__row contact__row--phone">
      <svg class="contact__icon" viewBox="0 0 20 20" aria-hidden="true"><rect width="20" height="20" rx="4" fill="var(--brand-charcoal)"/><path d="M6 4.5c.8-.5 1.6 0 2 .9l.8 1.6c.3.7 0 1.2-.5 1.6l-.6.4c.6 1.4 1.5 2.4 2.9 3l.4-.6c.4-.5.9-.8 1.6-.5l1.6.8c.9.4 1.3 1.2.9 2-.7 1.3-2.1 1.8-3.5 1.2C8.5 14 6 11.5 4.9 8.4 4.3 6.8 4.9 5.3 6 4.5Z" fill="#fff"/></svg>
      0427 531 068
    </li>
    <li class="contact__row contact__row--email">
      <svg class="contact__icon" viewBox="0 0 20 20" aria-hidden="true"><rect width="20" height="20" rx="4" fill="var(--brand-charcoal)"/><rect x="4" y="6" width="12" height="8.5" fill="#fff"/><path d="M4 6l6 5 6-5" fill="none" stroke="var(--brand-charcoal)" stroke-width="1.3"/></svg>
      tomp@harlowbuild-example.com.au
    </li>
    <li class="contact__row contact__row--web">
      <svg class="contact__icon" viewBox="0 0 20 20" aria-hidden="true"><rect width="20" height="20" rx="4" fill="var(--brand-charcoal)"/><path d="M10 4l6 5.5h-1.8V15h-3v-3.5H8.8V15h-3V9.5H4Z" fill="#fff"/></svg>
      harlowbuild-example.com.au
    </li>
  </ul>
</section>

<section class="card card--brand" aria-label="Business card, logo side">
  <div class="wordmark">Harlow Constructions</div>
</section>

</body>
</html>
```